KRV Business Card - Courier/Transportation - Needs Double Sided Business Card

I am searching for business cards for my company. Currently I just need cards for the (3) founders.

We are a new courier/transporation company that specializes in the medical/pharmaceutical arena.

As you will see from our logo, our primary colors are green and black. We strive to have an efficient, streamlined service offering. I like traditional looks, but also want to showcase our young, modern feel. I would like our card to be double sided.

Target Market(s)

Pharmacies
Hospitals
Physcian Office
Labs

Industry/Entity Type

Business

```html
<!DOCTYPE html>
<html lang="en">
<head>
<meta charset="utf-8">
<title>KRV Courier Business Card</title>
<link rel="stylesheet" href="https://fonts.googleapis.com/css2?family=Open+Sans:wght@400;600&display=swap">
<style>
  :root {
    --stage: #2b2b2b;
    --card-dark: #232222;
    --card-ink: #ffffff;
    --brand-green: #1f9a3c;
    --brand-green-soft: #2fb34e;
    --light-top: #ffffff;
    --light-bottom: #cfcfcf;
    --muted: #d9d9d9;
  }
  * { box-sizing: border-box; margin: 0; padding: 0; }
  html, body {
    width: 1200px; height: 900px; overflow: hidden;
    background: var(--stage);
    font-family: "Open Sans", Arial, sans-serif;
  }
  .canvas { position: relative; width: 1200px; height: 900px; }
  .card {
    position: absolute; width: 560px; height: 320px;
    background: var(--card-dark); overflow: hidden;
    box-shadow: 0 18px 40px rgba(0,0,0,.55);
  }
  .card--front { left: 80px; top: 120px; }
  .card--back { left: 560px; top: 460px; }

  /* Front */
  .brand {
    position: absolute; left: 0; right: 0; top: 118px;
    display: flex; align-items: center; justify-content: center; gap: 16px;
  }
  .brand__mark { width: 34px; height: 34px; background: var(--brand-green); }
  .brand__name {
    color: var(--brand-green-soft); font-weight: 600;
    font-size: 54px; letter-spacing: 4px; line-height: 1;
  }
  .brand__web {
    position: absolute; left: 0; right: 0; top: 196px;
    text-align: center; color: var(--muted); font-size: 13px; letter-spacing: 1px;
  }

  /* Back */
  .back__light {
    position: absolute; left: 0; right: 0; top: 150px; bottom: 0;
    background: linear-gradient(180deg, var(--light-top), var(--light-bottom));
  }
  .back__shape {
    position: absolute; left: 0; bottom: 0; width: 150px; height: 60px;
    background: #3a3a3a;
  }
  .contact { position: absolute; left: 26px; top: 26px; list-style: none; }
  .contact__item { margin-bottom: 6px; }
  .contact__label {
    display: block; color: var(--brand-green-soft);
    font-size: 11px; text-transform: uppercase; letter-spacing: .5px;
  }
  .contact__value { display: block; color: var(--card-ink); font-size: 13px; line-height: 1.3; }
  .person { position: absolute; right: 30px; top: 40px; text-align: left; }
  .person__name { color: var(--brand-green-soft); font-size: 28px; font-weight: 400; line-height: 1.05; }
  .person__role { color: var(--card-ink); font-size: 17px; }
  .back__brand {
    position: absolute; left: 170px; bottom: 56px;
    display: flex; align-items: center; gap: 14px;
  }
  .back__brand .brand__name { font-size: 58px; }
  .back__brand .brand__mark { width: 36px; height: 36px; }
</style>
</head>
<body>
<main class="canvas">
  <section class="card card--front" aria-label="Card front">
    <div class="brand">
      <span class="brand__mark"></span>
      <span class="brand__name">KRV COURIER</span>
    </div>
    <p class="brand__web">www.KRVcourier.net</p>
  </section>

  <section class="card card--back" aria-label="Card back">
    <div class="back__light"></div>
    <div class="back__shape"></div>
    <ul class="contact">
      <li class="contact__item">
        <span class="contact__label">Phone Number</span>
        <span class="contact__value">555 210 4820</span>
      </li>
      <li class="contact__item">
        <span class="contact__label">Email</span>
        <span class="contact__value">krv@example.com</span>
      </li>
      <li class="contact__item">
        <span class="contact__label">Address</span>
        <span class="contact__value">2408 Maple Crest Dr<br>Carmel, IN 46032</span>
      </li>
    </ul>
    <div class="person">
      <h2 class="person__name">YOUR NAME</h2>
      <p class="person__role">Company Position</p>
    </div>
    <div class="back__brand">
      <span class="brand__mark"></span>
      <span class="brand__name">KRV COURIER</span>
    </div>
  </section>
</main>
</body>
</html>
```